New Template design for Website in Wordpress

We are interested in changing our website look at www.haulvantix.com -We also are very interested in Have it done in Wordpress in which we are understanding the search engines are liking a bit more. The website we would want to try working with on this is www.haulvantix.com. We look forward to seeing the different design ideas please just make sure they are in wordpress! Thanks, Merrick

Reason: need more design idea..... We would still like to use our pictures off our site since we paid for them so keep that in mind as well as we would still want the rotating pictures in the head of the page but not in Flash.

```html
<!DOCTYPE html>
<html lang="en">
<head>
<meta charset="utf-8">
<title>Haulvantix – A diversified freight company</title>
<link href="https://fonts.googleapis.com/css2?family=Oswald:wght@400;500&family=Roboto:ital,wght@0,400;0,500;1,400&display=swap" rel="stylesheet">
<style>
:root{
  --blue:#1a9be0;
  --ink:#222222;
  --text:#333333;
  --panel:#e6eaee;
  --panel-line:#d3d9df;
  --band:#efefef;
  --footer:#2b2b2b;
  --footer-text:#a9a9a9;
  --white:#ffffff;
}
*{margin:0;padding:0;box-sizing:border-box}
html,body{width:696px;height:1200px;overflow:hidden;background:var(--white)}
body{position:relative;font-family:"Roboto",Arial,sans-serif;color:var(--text)}
.abs{position:absolute}
ul{list-style:none}

/* hero */
.hero{left:0;top:0;width:696px;height:278px;
  background:linear-gradient(180deg,#4a7699 0%,#5d86a6 40%,#7d8c9c 65%,#3d6486 100%)}
.header-bar{left:76px;top:14px;width:544px;height:42px;background:var(--ink);border-bottom:2px solid var(--blue)}
.brand{left:7px;top:6px;color:var(--white)}
.brand-name{font-family:"Oswald",sans-serif;font-size:15px;line-height:16px;color:var(--blue)}
.brand-tag{font-size:9px;line-height:12px;margin-top:1px}
.nav{right:0;top:0;height:40px;display:flex}
.nav a{display:block;height:40px;line-height:40px;padding:0 11px;font-size:7.6px;color:var(--white);text-decoration:none}
.nav a.active{background:var(--blue);padding:0 10px}
.hero-phone{left:268px;top:123px;width:160px;height:20px;background:var(--blue);color:var(--white);
  font-family:"Oswald",sans-serif;font-size:11px;line-height:20px;text-align:center}
.hero-title{left:0;top:148px;width:696px;text-align:center;color:var(--white);
  font-family:"Oswald",sans-serif;font-size:20px;line-height:30px}
.arrow{top:149px;width:23px;height:27px;background:var(--blue);display:flex;align-items:center;justify-content:center}

/* band */
.band{left:0;top:278px;width:696px;height:36px;background:var(--band)}
.band-title{left:84px;top:8px;font-family:"Oswald",sans-serif;font-size:14px;line-height:20px;color:var(--ink)}
.band-title em{font-family:"Roboto",sans-serif;font-style:italic;font-size:11.5px;color:#444}
.band-btn{left:491px;top:7px;width:122px;height:21px;background:var(--blue);border-radius:3px;color:var(--white);
  font-family:"Oswald",sans-serif;font-size:9px;line-height:21px;text-align:center}

/* services */
.service{top:328px;width:122px;height:84px;border:1px solid var(--blue)}
.service-photo{height:66px}
.service-caption{height:17px;background:var(--blue);color:var(--white);font-family:"Oswald",sans-serif;
  font-size:7.4px;line-height:17px;text-align:center;white-space:nowrap}

/* sidebar */
.side-box{left:84px;width:166px;background:var(--panel);border:1px solid var(--panel-line);padding:8px 6px 0 14px}
.side-head{display:flex;align-items:center;gap:6px;margin-left:-8px;margin-bottom:6px}
.side-title{font-family:"Oswald",sans-serif;font-size:10px;color:var(--ink);letter-spacing:-.1px}
.side-title span{color:var(--blue)}
.side-list li{font-size:7.2px;line-height:14px;color:var(--text);padding-left:6px;position:relative}
.side-list li::before{content:"›";position:absolute;left:0;top:-1px;color:var(--blue);font-size:9px;font-weight:500}

/* main */
.cta-bar{left:264px;top:427px;width:349px;height:25px;background:var(--ink);color:var(--white);
  font-family:"Oswald",sans-serif;font-size:11px;line-height:25px;text-align:center}
.main-title{left:264px;top:469px;font-family:"Oswald",sans-serif;font-size:15px;line-height:20px;color:var(--ink);font-weight:400}
.main-title span{color:var(--blue)}
.main-copy{left:264px;top:495px;width:349px;font-size:6.9px;line-height:9.8px;color:var(--text)}
.main-copy p+p{margin-top:9.5px}
.quote{left:264px;top:603px;width:349px;height:52px;background:var(--panel);border-left:3px solid var(--blue);
  padding:8px 8px 0 9px;font-family:"Oswald",sans-serif;font-size:11.4px;line-height:18px;color:var(--ink);font-weight:400}
.quote span{color:var(--blue)}

/* footer */
.footer{left:0;top:1103px;width:696px;height:97px;background:var(--footer)}
.foot-title{font-family:"Oswald",sans-serif;font-size:9px;color:var(--white)}
.foot-info{left:84px;top:14px;width:345px}
.foot-info p{font-size:5.6px;line-height:9.2px;color:var(--footer-text);margin-top:4px}
.foot-info p+p{margin-top:0}
.foot-sep{top:14px;width:0;height:76px;border-left:1px dotted #555}
.foot-pages{left:445px;top:14px}
.foot-pages li{font-size:5.8px;line-height:11.3px;color:var(--footer-text)}
.foot-pages ul{margin-top:4px}
.foot-follow{left:536px;top:14px}
.socials{display:flex;gap:4px;margin-top:6px}
.socials span{width:12px;height:12px;border-radius:2px}
</style>
</head>
<body>

<section class="abs hero" role="img" aria-label="Rotating header photo: loaded container ship sailing on blue open water"></section>

<header class="abs header-bar">
  <div class="abs brand">
    <div class="brand-name">Haulvantix</div>
    <div class="brand-tag">A diversified freight company</div>
  </div>
  <nav class="abs nav">
    <a class="active" href="#">Home</a>
    <a href="#">Insurance &amp; Legal Info</a>
    <a href="#">Fast Freight Quote</a>
  </nav>
</header>

<div class="abs hero-phone">Call (888)555-0142 – 7 Days Week</div>
<div class="abs hero-title">Get Fast &amp; Free Freight Quotes</div>
<div class="abs arrow" style="left:0">
  <svg width="12" height="10" viewBox="0 0 12 10"><path d="M6 1 2 5l4 4M11 1 7 5l4 4" fill="none" stroke="#fff" stroke-width="1.6"/></svg>
</div>
<div class="abs arrow" style="left:673px">
  <svg width="12" height="10" viewBox="0 0 12 10"><path d="M1 1l4 4-4 4M6 1l4 4-4 4" fill="none" stroke="#fff" stroke-width="1.6"/></svg>
</div>

<section class="abs band">
  <div class="abs band-title">WORLDWIDE SHIPPING - <em>Trucking and Ocean Service with No Limits</em></div>
  <div class="abs band-btn">CLICK HERE FOR FREIGHT QUOTE</div>
</section>

<div class="abs service" style="left:83px">
  <div class="service-photo" role="img" aria-label="Photo: heavy haul truck carrying large mining tires" style="background:linear-gradient(180deg,#8fb0c9 0%,#7d8a55 50%,#8c4a3a 100%)"></div>
  <div class="service-caption">Heavy Haul Services</div>
</div>
<div class="abs service" style="left:219px">
  <div class="service-photo" role="img" aria-label="Photo: white semi truck with refrigerated trailer" style="background:linear-gradient(180deg,#7fa7cf 0%,#dfe5ea 55%,#8a917f 100%)"></div>
  <div class="service-caption">Dry &amp; Refrigerated Services</div>
</div>
<div class="abs service" style="left:355px">
  <div class="service-photo" role="img" aria-label="Photo: blue truck pulling a flatbed trailer with a load" style="background:linear-gradient(180deg,#93b4cf 0%,#7b9a58 45%,#3f4f66 100%)"></div>
  <div class="service-caption">Flatbed, Step Deck &amp; Piggy Back Service</div>
</div>
<div class="abs service" style="left:491px">
  <div class="service-photo" role="img" aria-label="Photo: container ship at sea" style="background:linear-gradient(180deg,#b8c9d8 0%,#7f7f92 45%,#2f5575 100%)"></div>
  <div class="service-caption">Freight Forwarding Ocean Services</div>
</div>

<aside>
  <div class="abs side-box" style="top:427px;height:127px">
    <div class="side-head">
      <svg width="22" height="22" viewBox="0 0 22 22"><circle cx="11" cy="11" r="11" fill="var(--blue)"/><circle cx="11" cy="11" r="8.5" fill="none" stroke="#fff" stroke-width="1"/><path d="M6 12l10-5-3 9-2-3z" fill="#fff"/></svg>
      <div class="side-title">WORLDWIDE <span>Freight Services</span></div>
    </div>
    <ul class="side-list">
      <li>Worldwide Shipping Scope</li><li>Trucking Shipping Services</li><li>Ocean Shipping Services</li>
      <li>Insurance &amp; Legal Details</li><li>Get a Freight Quote Now!</li><li>Return to Home Page</li>
    </ul>
  </div>

  <div class="abs side-box" style="top:568px;height:137px">
    <div class="side-head">
      <svg width="22" height="22" viewBox="0 0 22 22"><circle cx="11" cy="11" r="11" fill="var(--blue)"/><circle cx="11" cy="11" r="8.5" fill="none" stroke="#fff" stroke-width="1"/><rect x="5" y="8" width="8" height="5" fill="#fff"/><path d="M13 9h2.5l1.5 2v2h-4z" fill="#fff"/><circle cx="7.5" cy="14" r="1.2" fill="#fff"/><circle cx="14.5" cy="14" r="1.2" fill="#fff"/></svg>
      <div class="side-title">FREIGHT <span>Trucking Service</span></div>
    </div>
    <ul class="side-list">
      <li>Heavy Equipment Hauling</li><li>LTL Freight Transport</li><li>Flatbed Transport</li><li>Step Deck Transport</li>
      <li>Dry Van Transport</li><li>Refrigerated Transport</li><li>Power Only &amp; Towaway Transport</li>
    </ul>
  </div>

  <div class="abs side-box" style="top:721px;height:137px">
    <div class="side-head">
      <svg width="22" height="22" viewBox="0 0 22 22"><circle cx="11" cy="11" r="11" fill="var(--blue)"/><circle cx="11" cy="11" r="8.5" fill="none" stroke="#fff" stroke-width="1"/><path d="M6 12h10l-2 3H8z" fill="#fff"/><rect x="8.5" y="7" width="5" height="4" fill="#fff"/></svg>
      <div class="side-title">OCEAN <span>Shipping Services</span></div>
    </div>
    <ul class="side-list">
      <li>Heavy Equipment Hauling</li><li>LTL Freight Transport</li><li>Flatbed Transport</li><li>Step Deck Transport</li>
      <li>Dry Van Transport</li><li>Refrigerated Transport</li><li>Power Only &amp; Towaway Transport</li>
    </ul>
  </div>

  <div class="abs side-box" style="top:875px;height:212px">
    <div class="side-head">
      <svg width="22" height="22" viewBox="0 0 22 22"><circle cx="11" cy="11" r="11" fill="var(--blue)"/><circle cx="11" cy="11" r="8.5" fill="none" stroke="#fff" stroke-width="1"/><rect x="6.5" y="8" width="9" height="7" fill="none" stroke="#fff" stroke-width="1.2"/><path d="M6.5 8l4.5 3.5L15.5 8" fill="none" stroke="#fff" stroke-width="1"/></svg>
      <div class="side-title">WE SHIP <span>It All Worldwide!</span></div>
    </div>
    <ul class="side-list">
      <li>Full Loads</li><li>LTL-Less Then Full Loads</li><li>Oversized &amp; Overweight Loads</li>
      <li>500 LBS to 200,000 LBS (No Limits)</li><li>Construction &amp; Mining Equipment</li><li>Mills &amp; Machinery</li>
      <li>Hay &amp; Alfalfa</li><li>Agriculture Equipment &amp; Commodities</li><li>Vehicles, Semi Tractors and Trailers</li>
      <li>Military and Non-Military Equipment</li><li>Refrigerated &amp; Dry Goods of All Kinds</li><li>Tanks, Waste Equipment, and More!</li>
    </ul>
  </div>
</aside>

<main>
  <div class="abs cta-bar">GET FAST &amp; FREE FREIGHT QUOTES NOW AND SAVE!!</div>
  <h1 class="abs main-title"><span>Worldwide shipping:</span> Ocean and Trucking with no limits</h1>
  <div class="abs main-copy">
    <p>Welcome to Haulvantix and Broadline Cargo Inc. We are a one stop solution logistics company servicing Worldwide with our Trucking and Ocean shipping service. In using our freight services, we will negotiate a competitive freight quote using over 5000 different carriers who are certified and contracted by us. We have all equipment types available daily, service all freight types, and have no limits Worldwide.</p>
    <p>Whether you need a freight quote for a full load, LTL/Partial load, or Oversized Machinery or Equipment, trucking and/or ocean shipment, we will take care of it. All your freight or equipment to be shipped will be covered in full by our insurance with no limitations to match its value. We manage the calls, the paperwork, and the headaches, and you get your freight moved with no hassles at a competitive shipping price!</p>
  </div>
  <div class="abs quote">Get your freight quote online now or call <span>888-555-0142</span> now and let some of the top carriers in the country compete for your business</div>
</main>

<footer class="abs footer">
  <div class="abs foot-info">
    <div class="foot-title">Important Information</div>
    <p>Full Loads, LTL, Oversized Machinery &amp; Equipment. We do it all. All freight covered to full value by our Insurance!</p>
    <p>All freight covered by a minimum of $1,000,000 in Liability and $200,000+ in Cargo Insurance with no limits Worldwide by both Truck and Ocean Carrier Services!</p>
    <p>Copyright and Owned by Broadline Cargo Inc. and Haulvantix.com–Equipment Transport Specialist</p>
  </div>
  <div class="abs foot-sep" style="left:431px"></div>
  <div class="abs foot-pages">
    <div class="foot-title">Popular Pages</div>
    <ul><li>Equipment Transport</li><li>Equipment Hauling</li><li>Shipping Service Areas</li></ul>
  </div>
  <div class="abs foot-sep" style="left:522px"></div>
  <div class="abs foot-follow">
    <div class="foot-title">Follow Us</div>
    <div class="socials" aria-label="Social links">
      <span style="background:#3b5a9a"></span><span style="background:#3a4d62"></span><span style="background:#f08a1c"></span><span style="background:#d2452f"></span><span style="background:#b02323"></span>
    </div>
  </div>
</footer>

</body>
</html>
```